Amber Ridge Partners Business Card

A business card design to accompany the logo design you completed on Pixel Forum. We are open to your proposals. I did add one idea below that might work, but we aren't married to the idea. The company is a real estate services company. Clientele are typically high net worth individuals, executive level employment or owners of their own company, 30-60 years old.

Our 1 (bad?) idea: double sided card; One side landscape with logo and word mark. Other side Portrait with the logo only (oversize watermark maybe?). Somewhere add text of Name (Marcus Tellingham), Title (Principal), phone # (555-214-7736) and email address (marcus@amberridgeco.example). There would be a second design with my wife's name, number and email in place of mine.

Again totally open to ideas here.

Industry/Entity Type

Real Estate

```html
<!DOCTYPE html>
<html lang="en">
<head>
<meta charset="utf-8">
<title>Amber Ridge Partners — Business Card</title>
<link rel="stylesheet" href="https://fonts.googleapis.com/css2?family=Cinzel:wght@400;500&family=Arimo:ital@0;1&display=swap">
<style>
  :root {
    --canvas: #e9e6e1;
    --card-green: #62975a;
    --sage-light: #abc8a2;
    --ink-white: #ffffff;
    --shadow: rgba(40, 30, 20, 0.18);
  }
  * { box-sizing: border-box; margin: 0; padding: 0; }
  html, body {
    width: 900px;
    height: 1200px;
    overflow: hidden;
    background: var(--canvas);
  }
  .canvas {
    position: relative;
    width: 900px;
    height: 1200px;
  }
  .card {
    position: absolute;
    left: 135px;
    width: 630px;
    height: 360px;
    background: var(--card-green);
    box-shadow: 0 8px 24px var(--shadow);
    overflow: hidden;
  }
  .card--front { top: 180px; }
  .card--back  { top: 660px; }

  /* Front: centred mark */
  .brand {
    position: absolute;
    inset: 0;
    display: flex;
    flex-direction: column;
    align-items: center;
    justify-content: center;
    gap: 26px;
  }
  .brand__square {
    width: 56px;
    height: 56px;
    background: var(--sage-light);
  }
  .brand__name {
    font-family: "Cinzel", serif;
    font-weight: 400;
    font-size: 30px;
    letter-spacing: 0.04em;
    color: var(--sage-light);
  }

  /* Back: oversized watermark area, bled off the left edge */
  .watermark {
    position: absolute;
    left: -30px;
    top: -20px;
    width: 370px;
    height: 400px;
    background: var(--sage-light);
  }

  /* Back: contact block */
  .contact {
    position: absolute;
    left: 366px;
    top: 244px;
    color: var(--ink-white);
    font-family: "Arimo", Arial, sans-serif;
    font-size: 15px;
    line-height: 1.3;
  }
  .contact__name {
    font-family: "Cinzel", serif;
    font-weight: 500;
    font-size: 22px;
    letter-spacing: 0.02em;
    line-height: 1.1;
    margin-bottom: 8px;
  }
  .contact__title { font-style: italic; }
</style>
</head>
<body>
  <main class="canvas">
    <section class="card card--front" aria-label="Card front">
      <div class="brand">
        <div class="brand__square" aria-hidden="true"></div>
        <p class="brand__name">Amber Ridge Partners</p>
      </div>
    </section>

    <section class="card card--back" aria-label="Card back">
      <div class="watermark" role="img" aria-label="Oversized faint brand mark watermark"></div>
      <div class="contact">
        <p class="contact__name">Marcus Tellingham</p>
        <p class="contact__title">Principal</p>
        <p class="contact__phone">555-214-7736</p>
        <p class="contact__email">marcus@amberridgeco.example</p>
      </div>
    </section>
  </main>
</body>
</html>
```